Brill Insurance Agency - Business Cards

Hello, I am needing new trendy business cards for our Insurance Agency now that I have a new Logo. I have attached our new logo with several color options along with a business card design that I like. I am leaning towards burgundy and blue colors. I have attached our current business card. I have also attached a headshot of our company president, Martin Vale, that you can use if you wish. Thank you so much in advance for all the wonderful designs!!!!

Target Market(s)

We want to look very professional to potential customers and we also want to look very professional so insurance companies will want to contract with us to sell their product.

Industry/Entity Type

Insurance

Contact Information for Business Card

Martin Vale
mvale@brillagency.com
Business: 555-213-4087
Fax: 555-213-7751
Cell: 555-390-2618
Toll Free: 888-555-0194
42 W Elm Rd Butler, MO 64730
www.brillagency.net

Font styles to use
Serif
Sans Serif

Colors
0355a3
3277b5
f04a50
ec1f27

Requirements
Nice to have
• I love creativity. The more creative and balanced a business card design the more I will like it. I would like the card to be printed horizontally instead of vertically.
Should not have
• My project should not have the Allied Coverage Network logo. It is no longer used in the industry.

```html
<!DOCTYPE html>
<html lang="en">
<head>
<meta charset="utf-8">
<title>Brill Insurance Agency – Business Cards</title>
<link rel="stylesheet" href="https://fonts.googleapis.com/css2?family=Montserrat:wght@700&family=Open+Sans:wght@400;600&display=swap">
<style>
  :root {
    --blue: #0355a3;
    --blue-light: #3277b5;
    --red: #ec1f27;
    --red-soft: #f04a50;
    --charcoal: #3f4650;
    --ink: #4a4f57;
    --paper: #ffffff;
    --backdrop: #ecebe8;
  }
  * { box-sizing: border-box; margin: 0; padding: 0; }
  html, body { width: 1200px; height: 1200px; overflow: hidden; }
  body {
    background: var(--backdrop);
    font-family: "Open Sans", Arial, sans-serif;
    position: relative;
  }
  .card {
    position: absolute;
    left: 180px;
    width: 840px;
    height: 480px;
    overflow: hidden;
    box-shadow: 0 6px 18px rgba(0,0,0,.12);
  }
  .card--front { top: 80px; background: var(--paper); }
  .card--back  { top: 640px; background: var(--blue); }

  .accent-bar {
    position: absolute; top: 0; right: 0;
    width: 370px; height: 40px;
    background: var(--blue);
  }
  .accent-bar::after {
    content: ""; position: absolute; left: 0; bottom: 0;
    width: 90px; height: 40px; background: var(--red);
  }
  .person-name {
    position: absolute; top: 86px; left: 500px;
    font-family: "Montserrat", Arial, sans-serif;
    font-weight: 700; font-size: 38px;
    color: var(--blue); letter-spacing: 0.5px;
    text-transform: uppercase; white-space: nowrap;
  }

  .agency-mark {
    position: absolute; display: flex; align-items: center; gap: 18px;
  }
  .agency-mark .dot {
    flex: none; border-radius: 50%;
  }
  .agency-mark .rule {
    flex: none; width: 1px; align-self: stretch;
  }
  .agency-mark .name {
    font-family: "Montserrat", Arial, sans-serif;
    font-weight: 700; line-height: 1.2;
    text-transform: uppercase; white-space: nowrap;
  }

  .card--front .agency-mark { left: 60px; top: 150px; }
  .card--front .agency-mark .dot { width: 44px; height: 44px; background: var(--red); }
  .card--front .agency-mark .rule { background: var(--charcoal); }
  .card--front .agency-mark .name { color: var(--blue); font-size: 24px; }

  .card--back .agency-mark {
    left: 50%; top: 50%; transform: translate(-50%, -50%); gap: 26px;
  }
  .card--back .agency-mark .dot {
    width: 96px; height: 96px; border: 11px solid var(--paper);
  }
  .card--back .agency-mark .rule { background: var(--paper); }
  .card--back .agency-mark .name { color: var(--paper); font-size: 36px; }

  .contact-list { position: absolute; list-style: none; }
  .contact-list li {
    display: flex; align-items: center; gap: 14px;
    font-size: 17px; color: var(--ink); height: 34px; white-space: nowrap;
  }
  .contact-list .icon { width: 20px; height: 20px; flex: none; color: var(--red); }
  .icon .solid { fill: currentColor; }
  .icon .line { fill: none; stroke: currentColor; stroke-width: 1.8; }
  .contact-list--left { left: 150px; top: 282px; }
  .contact-list--right { left: 520px; top: 200px; }

  .divider {
    position: absolute; left: 470px; top: 190px;
    width: 1px; height: 130px; background: var(--charcoal);
  }
  .address-band {
    position: absolute; left: 0; right: 0; bottom: 0; height: 56px;
    background: var(--charcoal); color: var(--paper);
    border-top: 4px solid var(--blue-light);
    display: flex; align-items: center; justify-content: center;
    font-size: 20px; letter-spacing: 0.3px;
  }
</style>
</head>
<body>

<section class="card card--front" aria-label="Business card front">
  <div class="accent-bar"></div>
  <h1 class="person-name">Martin Vale</h1>

  <div class="agency-mark">
    <span class="dot"></span>
    <span class="rule"></span>
    <span class="name">Brill Insurance<br>Agency Inc</span>
  </div>

  <ul class="contact-list contact-list--left">
    <li><svg class="icon" viewBox="0 0 20 20"><path class="line" d="M1 4h18v12H1z M1 4l9 7 9-7"/></svg>mvale@brillagency.com</li>
    <li><svg class="icon" viewBox="0 0 20 20"><path class="solid" d="M4 1l4 1 1 4-2 2c1 2 3 4 5 5l2-2 4 1 1 4-2 2C9 18 2 11 2 3z"/></svg>555-213-4087</li>
    <li><svg class="icon" viewBox="0 0 20 20"><path class="solid" d="M5 1h10v5H5z M2 7h16v8H2z M5 12h10v7H5z"/></svg>555-213-7751</li>
  </ul>

  <div class="divider"></div>

  <ul class="contact-list contact-list--right">
    <li><svg class="icon" viewBox="0 0 20 20"><path class="solid" d="M10 2l9 8h-3v8h-4v-5H8v5H4v-8H1z"/></svg>555-390-2618</li>
    <li><svg class="icon" viewBox="0 0 20 20"><circle class="line" cx="10" cy="10" r="8.5"/><path class="solid" d="M7 5l2 .5.5 2-1 1c.6 1 1.4 1.8 2.4 2.4l1-1 2 .5.5 2-1 1C9 13 6 10 6 6z"/></svg>888-555-0194</li>
    <li><svg class="icon" viewBox="0 0 20 20"><circle class="line" cx="10" cy="10" r="8.5"/><ellipse class="line" cx="10" cy="10" rx="3.5" ry="8.5"/><path class="line" d="M1.5 10h17M3 5.5h14M3 14.5h14"/></svg>www.brillagency.net</li>
  </ul>

  <div class="address-band">42 W Elm Rd Butler, MO 64730</div>
</section>

<section class="card card--back" aria-label="Business card back">
  <div class="agency-mark">
    <span class="dot"></span>
    <span class="rule"></span>
    <span class="name">Brill Insurance<br>Agency Inc</span>
  </div>
</section>

</body>
</html>
```